Clausewise - Training I Consulting I Review - Related to Contracts/Agreements

We provide legal services, we need a plattform to book video online trainings or local trainings classes and appointments (with calendar feature to select date and see availability at screen), payment over internet, legal document creation over webpage, videos will be produces in the next 3 - 4 moths so this is a place holder item. Participants for the Online trainings shall have a login in area with secured password. Appointments for local trainings and Consulting. Consider Outline in file attached. I can send you also a video with more explanation regarding the purpose.

Target Market(s)

Startup/scale up Software companies that intent to have an international business and need help with their contracts, to sell their products. Sales persons.

Industry/Entity Type

Legal

Coding

Coded - Design and coding required

Number of Pages Required

5+ page

Font styles to use
Serif
Sans Serif

Colors
000000
eeeeee
f5f5f5
ffffff
f8fcfd
3277b5
ecf7fb
cadf82
86cfc6

Requirements
Must have
• See file clausewise attached with outline. Moreover see here first starting point: https://tomas-vendrell.pagebuildr.example/mysite-1 . Main inspiration comes from www.advisoryhub.example from the log in area, see the outline in the file attached with the screen shots. At the end I need someone who can draft the full webpage and maintain it for a yearly fee. It must be simple and well structured layout. Lean. 1st landing page shall not scroll, 2 landing page only a little to see the testimonials and foster of page. There should be a Progress Bar to indicate the booking/selection process. Calendar booking. Easy fast booking.
• I like the colour mix, the feeling and the easy structor of:
• https://www.artmarket.example/design/6374387or
• https://www.artmarket.example/design/6372391 or https://www.artmarket.example/design/6374366
• https://www.vendorgrid.example/en/web-design/belgium-be
• https://www.artmarket.example/design/5896857
• https://www.artmarket.example/design/5902173
• https://www.artmarket.example/design/17197349
• https://www.artmarket.example/design/5464461
• https://www.artmarket.example/design/7180908
Nice to have
• page for evaluation and interview, see outline attached in the file with screen shots. Document upload.
Should not have
• many pictures, long scroll down pages on the 1st and 2nd ladding pages, many colours and forms. No need for news letter, search field, no need for links to Chatterly and other social media (except workNet).

```html
<!DOCTYPE html>
<html lang="en">
<head>
<meta charset="utf-8">
<title>Clausewise – Choose your Service</title>
<link rel="stylesheet" href="https://fonts.googleapis.com/css2?family=Figtree:wght@400;500;600&family=Playfair+Display:wght@500&display=swap">
<style>
  :root {
    --ink: #2f2f2f;
    --header-bg: #333333;
    --panel-bg: #f5f5f5;
    --page-bg: #ffffff;
    --card-border: #e6e6e6;
    --muted: #8a8a8a;
    --text-dark: #3a3f4a;
    --accent: #6fc3e3;
    --accent-light: #9bd8ee;
    --star: #6cc2e0;
    --dot: #c8c8c8;
    --rule: #d8d8d8;
    --footer-link: #d9d9d9;
  }
  * { box-sizing: border-box; margin: 0; padding: 0; }
  html, body { width: 1200px; height: 1031px; overflow: hidden; }
  body {
    position: relative;
    background: var(--page-bg);
    font-family: "Figtree", "Helvetica Neue", Arial, sans-serif;
    color: var(--ink);
  }

  /* Header */
  .site-header {
    position: absolute; left: 0; top: 0; width: 1200px; height: 64px;
    background: var(--header-bg);
  }
  .brand {
    position: absolute; left: 156px; top: 12px;
    font-family: "Playfair Display", Georgia, serif; font-weight: 500;
    font-size: 34px; color: #ffffff; letter-spacing: 0.2px;
  }
  .nav-link {
    position: absolute; top: 22px; font-size: 15px; font-weight: 500; color: #ffffff;
    text-decoration: none;
  }
  .nav-link.refer { left: 550px; display: flex; align-items: center; gap: 7px; }
  .nav-link.services { left: 733px; color: var(--accent); }
  .nav-link.services::after {
    content: ""; position: absolute; left: -7px; right: -7px; top: 38px; height: 3px;
    background: var(--accent);
  }
  .nav-link.partner { left: 842px; }
  .login-btn {
    position: absolute; left: 931px; top: 16px; width: 112px; height: 32px;
    background: linear-gradient(#a5dcef, var(--accent));
    border-radius: 2px; color: #ffffff; font-size: 14px;
    display: flex; align-items: center; justify-content: center; gap: 6px;
  }

  /* Services */
  .services-panel {
    position: absolute; left: 0; top: 64px; width: 1200px; height: 469px;
    background: var(--panel-bg);
    box-shadow: 0 4px 8px rgba(0,0,0,0.06);
  }
  .section-title {
    position: absolute; left: 0; width: 1200px; top: 58px; text-align: center;
    font-size: 27px; font-weight: 400; color: #222;
  }
  .service-card {
    position: absolute; top: 124px; width: 280px; height: 280px;
    background: #ffffff; border: 1px solid var(--card-border);
  }
  .service-card:nth-of-type(1) { left: 156px; }
  .service-card:nth-of-type(2) { left: 460px; }
  .service-card:nth-of-type(3) { left: 764px; }
  .card-head {
    height: 57px; background: var(--header-bg); color: #ffffff;
    font-size: 22px; text-align: center; line-height: 50px; font-weight: 400;
  }
  .card-icon {
    position: absolute; left: 114px; top: 45px; width: 52px; height: 52px;
    border-radius: 50%; background: #ffffff; border: 2px solid #111;
    display: flex; align-items: center; justify-content: center;
  }
  .card-text {
    position: absolute; left: 20px; right: 20px; top: 120px;
    text-align: center; font-size: 13px; line-height: 19.2px; color: var(--muted);
  }
  .card-btn {
    position: absolute; left: 76px; top: 221px; width: 128px; height: 33px;
    border-radius: 2px; color: #ffffff; font-size: 13px;
    display: flex; align-items: center; justify-content: center;
    background: linear-gradient(#5a5a5a, #2e2e2e);
    box-shadow: 0 1px 2px rgba(0,0,0,0.3);
  }
  .card-btn.is-active { background: linear-gradient(#a5dcef, var(--accent)); box-shadow: none; }

  /* Testimonials */
  .testimonial {
    position: absolute; top: 596px; width: 304px; height: 178px;
  }
  .testimonial:nth-of-type(1) { left: 144px; }
  .testimonial:nth-of-type(2) { left: 448px; border-left: 1px solid var(--rule); }
  .testimonial:nth-of-type(3) { left: 752px; border-left: 1px solid var(--rule); }
  .avatar {
    position: absolute; left: 36px; top: 24px; width: 48px; height: 48px; border-radius: 50%;
  }
  .testimonial:nth-of-type(2) .avatar { left: 35px; background: linear-gradient(#c9a58d, #8f6a55); }
  .testimonial:nth-of-type(1) .avatar { background: linear-gradient(#b7b9bd, #3d3f46); }
  .testimonial:nth-of-type(3) .avatar { background: linear-gradient(#a29487, #3a3430); }
  .stars { position: absolute; left: 104px; top: 22px; display: flex; gap: 6px; }
  .quote {
    position: absolute; left: 104px; top: 46px; width: 180px;
    font-size: 13px; line-height: 19.2px; color: var(--muted);
  }
  .author {
    position: absolute; left: 104px; top: 140px; font-size: 14px; font-weight: 500;
    color: var(--text-dark); letter-spacing: 0.3px;
  }
  .testimonial:nth-of-type(2) .stars,
  .testimonial:nth-of-type(2) .quote,
  .testimonial:nth-of-type(2) .author { left: 104px; }
  .carousel-dots { position: absolute; top: 814px; left: 579px; display: flex; gap: 9px; }
  .carousel-dots span { width: 8px; height: 8px; border-radius: 50%; background: var(--dot); }
  .carousel-dots span.current { background: var(--accent); }

  /* Footer */
  .site-footer {
    position: absolute; left: 0; top: 888px; width: 1200px; height: 143px;
    background: var(--header-bg);
  }
  .footer-col { position: absolute; top: 27px; display: flex; flex-direction: column; gap: 9px; }
  .footer-col a { color: var(--footer-link); font-size: 13px; text-decoration: none; line-height: 15px; }
  .footer-col.c1 { left: 156px; top: 29px; }
  .footer-col.c2 { left: 284px; top: 29px; }
  .footer-col.c3 { left: 377px; top: 27px; }
  .footer-col.c4 { left: 445px; top: 27px; }
  .footer-brand {
    position: absolute; left: 560px; top: 32px; width: 120px; text-align: center;
    font-size: 20px; font-weight: 600; color: #1e1e1e; letter-spacing: 0.5px;
  }
  .appointment-btn {
    position: absolute; left: 763px; top: 30px; width: 203px; height: 33px;
    background: linear-gradient(#a5dcef, var(--accent)); color: #ffffff; font-size: 13px;
    display: flex; align-items: center; justify-content: center; border-radius: 1px;
  }
  .social {
    position: absolute; left: 1004px; top: 26px; width: 40px; height: 40px; border-radius: 50%;
    background: #4a4a4a; box-shadow: 0 1px 3px rgba(0,0,0,0.5);
  }
  .footer-rule { position: absolute; left: 132px; top: 96px; width: 936px; height: 1px; background: #6a6a6a; }
  .copyright {
    position: absolute; left: 0; width: 1200px; top: 111px; text-align: center;
    font-size: 13px; color: #e5e5e5; letter-spacing: 0.2px;
  }
  .copyright em { font-style: normal; color: var(--accent); }
</style>
</head>
<body>

<header class="site-header">
  <div class="brand">Clausewise</div>
  <a class="nav-link refer" href="#">
    <svg width="16" height="13" viewBox="0 0 16 13" aria-hidden="true">
      <circle cx="5" cy="3.5" r="3" fill="#e4474b"/><path d="M0 13c0-4 2-6 5-6s5 2 5 6z" fill="#e4474b"/>
      <circle cx="11.5" cy="3.5" r="2.6" fill="#e4474b"/><path d="M10 7.3c3 0 6 1.5 6 5.7h-5c0-2.5-.5-4.2-1-5.7z" fill="#e4474b"/>
    </svg>
    Refere Someone
  </a>
  <a class="nav-link services" href="#">Services</a>
  <a class="nav-link partner" href="#">Partner</a>
  <div class="login-btn">
    <svg width="9" height="11" viewBox="0 0 9 11" aria-hidden="true"><circle cx="4.5" cy="3" r="2.6" fill="#fff"/><path d="M0 11c0-3 2-4.5 4.5-4.5S9 8 9 11z" fill="#fff"/></svg>
    Login
  </div>
</header>

<main>
  <section class="services-panel">
    <h1 class="section-title">Choose your Service</h1>

    <article class="service-card">
      <h2 class="card-head">Contract Training</h2>
      <div class="card-icon">
        <svg width="28" height="28" viewBox="0 0 28 28" aria-hidden="true">
          <rect x="12" y="3" width="14" height="10" fill="none" stroke="#111" stroke-width="1.6"/>
          <circle cx="7" cy="5" r="2.3" fill="#111"/><path d="M4 15v-6h6l4-2v1.5l-4 2.5v4z" fill="#111"/>
          <circle cx="5" cy="19" r="1.8" fill="#111"/><circle cx="11" cy="19" r="1.8" fill="#111"/><circle cx="17" cy="19" r="1.8" fill="#111"/><circle cx="23" cy="19" r="1.8" fill="#111"/>
          <path d="M2 26c0-3 1.5-4 3-4s3 1 3 4zM8 26c0-3 1.5-4 3-4s3 1 3 4zM14 26c0-3 1.5-4 3-4s3 1 3 4zM20 26c0-3 1.5-4 3-4s3 1 3 4z" fill="#111"/>
        </svg>
      </div>
      <p class="card-text">There are many variations of the passages of Lorem Ipsum available,but the majority have suffered words If you are going to use are the Lorem...</p>
      <div class="card-btn">Book Now!</div>
    </article>

    <article class="service-card">
      <h2 class="card-head">Contract Design</h2>
      <div class="card-icon">
        <svg width="28" height="28" viewBox="0 0 28 28" aria-hidden="true">
          <rect x="9" y="11" width="10" height="9" rx="1" fill="#111"/>
          <circle cx="14" cy="5" r="2.6" fill="#111"/><circle cx="6" cy="9" r="2.4" fill="#111"/><circle cx="22" cy="9" r="2.4" fill="#111"/>
          <path d="M2 20v-5c0-1.5 1.5-2.5 4-2.5v7.5zM26 20v-5c0-1.5-1.5-2.5-4-2.5v7.5z" fill="#111"/>
          <circle cx="8" cy="23" r="2" fill="#111"/><circle cx="20" cy="23" r="2" fill="#111"/>
        </svg>
      </div>
      <p class="card-text">There are many variations of the passages of Lorem Ipsum available,but the majority have suffered words If you are going to use are the Lorem...</p>
      <div class="card-btn is-active">Select</div>
    </article>

    <article class="service-card">
      <h2 class="card-head">Template Online</h2>
      <div class="card-icon">
        <svg width="28" height="28" viewBox="0 0 28 28" aria-hidden="true">
          <rect x="3" y="4" width="22" height="20" rx="1.5" fill="none" stroke="#111" stroke-width="1.8"/>
          <rect x="3" y="4" width="22" height="4" fill="#111"/>
          <path d="M7 12h8M7 15h6M7 18h8" stroke="#111" stroke-width="1.6"/>
          <path d="M15 21l8-9 2 2-8 9-3 1z" fill="#111"/>
        </svg>
      </div>
      <p class="card-text">There are many variations of the passages of Lorem Ipsum available,but the majority have suffered words If you are going to use are the Lorem...</p>
      <div class="card-btn">Select</div>
    </article>
  </section>

  <section class="testimonials">
    <article class="testimonial">
      <div class="avatar" role="img" aria-label="Portrait photo of the reviewer"></div>
      <div class="stars">
        <svg width="15" height="14" viewBox="0 0 20 19"><polygon points="10,0 12.9,6.2 20,7 14.7,11.8 16.2,19 10,15.3 3.8,19 5.3,11.8 0,7 7.1,6.2" fill="var(--star)"/></svg>
        <svg width="15" height="14" viewBox="0 0 20 19"><polygon points="10,0 12.9,6.2 20,7 14.7,11.8 16.2,19 10,15.3 3.8,19 5.3,11.8 0,7 7.1,6.2" fill="var(--star)"/></svg>
        <svg width="15" height="14" viewBox="0 0 20 19"><polygon points="10,0 12.9,6.2 20,7 14.7,11.8 16.2,19 10,15.3 3.8,19 5.3,11.8 0,7 7.1,6.2" fill="var(--star)"/></svg>
        <svg width="15" height="14" viewBox="0 0 20 19"><polygon points="10,0 12.9,6.2 20,7 14.7,11.8 16.2,19 10,15.3 3.8,19 5.3,11.8 0,7 7.1,6.2" fill="var(--star)"/></svg>
        <svg width="15" height="14" viewBox="0 0 20 19"><polygon points="10,0 12.9,6.2 20,7 14.7,11.8 16.2,19 10,15.3 3.8,19 5.3,11.8 0,7 7.1,6.2" fill="var(--star)"/></svg>
      </div>
      <p class="quote">Contrary to popular belief, Lorem Ipsum is not simply random text. It has roots in a piece of classical.</p>
      <p class="author">Standard Chunk</p>
    </article>

    <article class="testimonial">
      <div class="avatar" role="img" aria-label="Portrait photo of the reviewer"></div>
      <div class="stars">
        <svg width="15" height="14" viewBox="0 0 20 19"><polygon points="10,0 12.9,6.2 20,7 14.7,11.8 16.2,19 10,15.3 3.8,19 5.3,11.8 0,7 7.1,6.2" fill="var(--star)"/></svg>
        <svg width="15" height="14" viewBox="0 0 20 19"><polygon points="10,0 12.9,6.2 20,7 14.7,11.8 16.2,19 10,15.3 3.8,19 5.3,11.8 0,7 7.1,6.2" fill="var(--star)"/></svg>
        <svg width="15" height="14" viewBox="0 0 20 19"><polygon points="10,0 12.9,6.2 20,7 14.7,11.8 16.2,19 10,15.3 3.8,19 5.3,11.8 0,7 7.1,6.2" fill="var(--star)"/></svg>
        <svg width="15" height="14" viewBox="0 0 20 19"><polygon points="10,0 12.9,6.2 20,7 14.7,11.8 16.2,19 10,15.3 3.8,19 5.3,11.8 0,7 7.1,6.2" fill="var(--star)"/></svg>
        <svg width="15" height="14" viewBox="0 0 20 19"><polygon points="10,0 12.9,6.2 20,7 14.7,11.8 16.2,19 10,15.3 3.8,19 5.3,11.8 0,7 7.1,6.2" fill="var(--star)"/></svg>
      </div>
      <p class="quote">Contrary to popular belief, Lorem Ipsum is not simply random text. It has roots in a piece of classical.</p>
      <p class="author">H. Marlowe.</p>
    </article>

    <article class="testimonial">
      <div class="avatar" role="img" aria-label="Portrait photo of the reviewer"></div>
      <div class="stars">
        <svg width="15" height="14" viewBox="0 0 20 19"><polygon points="10,0 12.9,6.2 20,7 14.7,11.8 16.2,19 10,15.3 3.8,19 5.3,11.8 0,7 7.1,6.2" fill="var(--star)"/></svg>
        <svg width="15" height="14" viewBox="0 0 20 19"><polygon points="10,0 12.9,6.2 20,7 14.7,11.8 16.2,19 10,15.3 3.8,19 5.3,11.8 0,7 7.1,6.2" fill="var(--star)"/></svg>
        <svg width="15" height="14" viewBox="0 0 20 19"><polygon points="10,0 12.9,6.2 20,7 14.7,11.8 16.2,19 10,15.3 3.8,19 5.3,11.8 0,7 7.1,6.2" fill="var(--star)"/></svg>
        <svg width="15" height="14" viewBox="0 0 20 19"><polygon points="10,0 12.9,6.2 20,7 14.7,11.8 16.2,19 10,15.3 3.8,19 5.3,11.8 0,7 7.1,6.2" fill="var(--star)"/></svg>
        <svg width="15" height="14" viewBox="0 0 20 19"><polygon points="10,0 12.9,6.2 20,7 14.7,11.8 16.2,19 10,15.3 3.8,19 5.3,11.8 0,7 7.1,6.2" fill="var(--star)"/></svg>
      </div>
      <p class="quote">Contrary to popular belief, Lorem Ipsum is not simply random text. It has roots in a piece of classical.</p>
      <p class="author">Finibus Bonorum</p>
    </article>

    <div class="carousel-dots"><span></span><span class="current"></span><span></span></div>
  </section>
</main>

<footer class="site-footer">
  <nav class="footer-col c1"><a href="#">Evaluation</a><a href="#">Market Feedback</a></nav>
  <nav class="footer-col c2"><a href="#">Students</a><a href="#">Templates</a></nav>
  <nav class="footer-col c3"><a href="#">Policies</a><a href="#">Tools</a></nav>
  <nav class="footer-col c4"><a href="#">Team</a><a href="#">Contact</a></nav>
  <div class="footer-brand">Clausewise</div>
  <div class="appointment-btn">Make an Appointment</div>
  <a class="social" href="#" aria-label="workNet"></a>
  <div class="footer-rule"></div>
  <p class="copyright">© 2018 <em>Clausewise</em> All Right Reserved.</p>
</footer>

</body>
</html>
```